Business Card

Just need business logo with phone number on it. 0487 312 556
And the following on the bottom of the card.

"Your local plumbing experts".
and emblems for kelpa card, cheque and cash

```html
<!DOCTYPE html>
<html lang="en">
<head>
<meta charset="utf-8">
<title>Ridgeline Plumbing &amp; Drainage – Business Card</title>
<link rel="stylesheet" href="https://fonts.googleapis.com/css2?family=Montserrat:wght@500;600;800&display=swap">
<style>
  :root {
    --brand-red: #e8232e;
    --brand-red-soft: rgba(232, 35, 46, 0.55);
    --brand-blue: #1e8fd0;
    --brand-blue-light: #3aa6e2;
    --brand-blue-deep: #1886c7;
    --paper: #ffffff;
    --backdrop: #e9e6e1;
    --shadow: rgba(0, 0, 0, 0.28);
  }
  * { box-sizing: border-box; margin: 0; padding: 0; }
  html, body {
    width: 900px; height: 1200px; overflow: hidden;
    background: var(--backdrop);
    font-family: "Montserrat", Arial, sans-serif;
  }
  .card {
    position: absolute; left: 87px; width: 735px; height: 429px;
    border-radius: 24px; overflow: hidden;
    box-shadow: 0 6px 16px var(--shadow);
  }
  .card--front { top: 137px; background: var(--paper); }
  .card--back {
    top: 633px;
    background: radial-gradient(ellipse at 85% 20%, var(--brand-blue-light) 0%, var(--brand-blue-deep) 65%);
  }

  .card__swoosh {
    position: absolute; left: 0; right: 0; top: 238px; height: 62px;
    background: linear-gradient(to bottom,
      rgba(255, 255, 255, 0) 0%,
      var(--brand-red-soft) 40%,
      var(--brand-blue-light) 80%,
      var(--brand-blue) 100%);
  }
  .card__footer-band {
    position: absolute; left: 0; right: 0; top: 300px; bottom: 0;
    background: var(--brand-blue);
  }

  .wordmark {
    position: absolute; left: 0; right: 0; text-align: center;
    font-weight: 800; text-transform: uppercase; line-height: 1.05;
  }
  .card--front .wordmark { top: 52px; color: var(--brand-red); }
  .card--back .wordmark { top: 170px; color: var(--paper); }
  .wordmark__name { display: block; font-size: 64px; letter-spacing: 2px; }
  .wordmark__trade { display: block; font-size: 27px; letter-spacing: 5px; margin-top: 6px; }
  .card--back .wordmark__name { font-size: 46px; }
  .card--back .wordmark__trade { font-size: 19px; letter-spacing: 4px; }

  .tagline {
    position: absolute; top: 216px; left: 0; right: 0; text-align: center;
    color: var(--brand-blue); font-weight: 600; font-size: 18px; letter-spacing: 1.5px;
  }

  .payments { position: absolute; left: 44px; top: 356px; color: var(--paper); }
  .payments__label {
    display: flex; align-items: center; gap: 6px;
    font-size: 13px; font-weight: 500; letter-spacing: 0.5px;
  }
  .payments__label::before, .payments__label::after {
    content: ""; width: 26px; height: 1px; background: var(--paper);
  }
  .payments__icons { display: flex; gap: 16px; margin-top: 8px; align-items: center; }
  .pay-card {
    width: 46px; height: 28px; background: var(--paper); border-radius: 2px;
    color: var(--brand-blue-deep); font-size: 12px; font-weight: 800;
    display: flex; align-items: center; justify-content: center;
  }

  .contact {
    position: absolute; right: 48px; top: 368px;
    display: flex; align-items: center; gap: 12px;
    color: var(--paper); font-size: 25px; font-weight: 600; letter-spacing: 1.5px;
  }
</style>
</head>
<body>

<section class="card card--front">
  <div class="card__swoosh" role="img" aria-label="Red and blue flowing swoosh band"></div>
  <div class="card__footer-band"></div>

  <h1 class="wordmark">
    <span class="wordmark__name">Ridgeline</span>
    <span class="wordmark__trade">Plumbing &amp; Drainage</span>
  </h1>

  <p class="tagline">YOUR LOCAL PLUMBING EXPERTS</p>

  <div class="payments">
    <p class="payments__label">WE ACCEPT</p>
    <div class="payments__icons">
      <span class="pay-card">kelpa</span>
      <svg class="pay-cash" width="46" height="28" viewBox="0 0 46 28" aria-label="Cash">
        <rect x="6" y="2" width="38" height="20" rx="2" fill="none" stroke="var(--paper)" stroke-width="2" transform="rotate(-8 25 12)"/>
        <rect x="2" y="6" width="38" height="20" rx="2" fill="var(--paper)" transform="rotate(-8 21 16)"/>
        <text x="21" y="22" text-anchor="middle" font-size="14" font-weight="800" fill="var(--brand-blue)" font-family="Montserrat, sans-serif">$</text>
      </svg>
      <svg class="pay-cheque" width="46" height="28" viewBox="0 0 46 28" aria-label="Cheque">
        <rect x="1" y="3" width="36" height="23" rx="2" fill="none" stroke="var(--paper)" stroke-width="2"/>
        <text x="9" y="21" text-anchor="middle" font-size="13" font-weight="800" fill="var(--paper)" font-family="Montserrat, sans-serif">$</text>
        <line x1="17" y1="12" x2="29" y2="12" stroke="var(--paper)" stroke-width="2"/>
        <line x1="17" y1="18" x2="27" y2="18" stroke="var(--paper)" stroke-width="2"/>
        <path d="M28,20 L42,4 L45,7 L31,23 L27,24 Z" fill="var(--paper)"/>
      </svg>
    </div>
  </div>

  <div class="contact">
    <svg width="26" height="26" viewBox="0 0 26 26" aria-label="Phone">
      <rect width="26" height="26" rx="4" fill="var(--paper)"/>
      <path fill="var(--brand-blue)" d="M8.2,5.5 L10.6,5.5 L11.8,9.4 L10.2,10.8 C11,12.8 13.2,15 15.2,15.8 L16.6,14.2 L20.5,15.4 L20.5,17.8 C20.5,19 19.5,20.5 18,20.5 C11.5,20.3 5.7,14.5 5.5,8 C5.5,6.5 7,5.5 8.2,5.5 Z"/>
    </svg>
    <span class="contact__phone">0487 312 556</span>
  </div>
</section>

<section class="card card--back">
  <h2 class="wordmark">
    <span class="wordmark__name">Ridgeline</span>
    <span class="wordmark__trade">Plumbing &amp; Drainage</span>
  </h2>
</section>

</body>
</html>
```